ORB Stationary and Biz cards
Please include the logo I have attached.
Simple
Dorotea Wellmont
dpalvane@qzr.example
www.orbworthkeeping.example
Hello,
I will provide the proper address in a few days. It will take one line for address and one for city and state.
I uploaded the entire file of my logo, not only the AI format. Please let me know if this is a problem. Thank you!
Please let me know if you cannot access the subfiles within this file for your use. Thanks!
Please let me know if you have problems opening the AI file in this attachment. Thank you!
ORB

```html
<!DOCTYPE html>
<html lang="en">
<head>
<meta charset="utf-8">
<title>ORB Business Card</title>
<link href="https://fonts.googleapis.com/css2?family=Open+Sans:wght@400;600;700&display=swap" rel="stylesheet">
<style>
  :root {
    --page-bg: #dcdcdc;
    --card-top: #ffffff;
    --card-top-shade: #e9eaec;
    --brand-blue: #1f6fc4;
    --band-blue-light: #2a93dc;
    --band-blue-dark: #1b62b8;
    --swoosh-green: #6cbf2a;
    --swoosh-green-light: #9ad34a;
    --text-light: #ffffff;
  }
  * { margin: 0; padding: 0; box-sizing: border-box; }
  html, body {
    width: 1200px;
    height: 770px;
    overflow: hidden;
    background: var(--page-bg);
    font-family: "Open Sans", Arial, sans-serif;
  }
  .business-card {
    position: absolute;
    left: 60px;
    top: 105px;
    width: 1080px;
    height: 560px;
    border-radius: 34px;
    overflow: hidden;
    background: radial-gradient(ellipse at 45% 20%, var(--card-top) 0%, var(--card-top-shade) 100%);
    box-shadow: 0 6px 18px rgba(0,0,0,0.18);
  }
  .card-waves {
    position: absolute;
    inset: 0;
    width: 100%;
    height: 100%;
  }
  .brand-lockup {
    position: absolute;
    left: 300px;
    top: 62px;
    display: flex;
    align-items: center;
    gap: 14px;
  }
  .brand-square {
    width: 26px;
    height: 26px;
    background: var(--brand-blue);
  }
  .brand-name {
    font-size: 64px;
    font-weight: 700;
    color: var(--brand-blue);
    line-height: 1;
    letter-spacing: 2px;
  }
  .contact-list {
    position: absolute;
    left: 40px;
    top: 388px;
    list-style: none;
    color: var(--text-light);
    font-size: 17px;
    line-height: 24px;
  }
  .contact-list li {
    display: flex;
    align-items: flex-start;
    gap: 12px;
  }
  .contact-list .contact-icon {
    flex: none;
    width: 17px;
    height: 17px;
    margin-top: 3px;
  }
  .contact-list .address-line-two {
    padding-left: 29px;
  }
  .card-holder {
    position: absolute;
    right: 44px;
    top: 470px;
    text-align: right;
    color: var(--text-light);
  }
  .holder-name {
    font-size: 20px;
    font-weight: 700;
    line-height: 26px;
  }
  .holder-role {
    font-size: 18px;
    font-weight: 400;
    line-height: 24px;
  }
</style>
</head>
<body>
  <div class="business-card">
    <svg class="card-waves" viewBox="0 0 1080 560" preserveAspectRatio="none" aria-hidden="true">
      <defs>
        <linearGradient id="band-gradient" x1="0" y1="0" x2="0" y2="1">
          <stop offset="0" stop-color="var(--band-blue-light)"/>
          <stop offset="1" stop-color="var(--band-blue-dark)"/>
        </linearGradient>
      </defs>
      <path d="M0 262 C 180 250, 330 330, 560 375 C 760 412, 930 440, 1080 470 L1080 560 L0 560 Z" fill="url(#band-gradient)"/>
      <path d="M0 250 C 200 236, 360 300, 560 330 C 760 360, 920 400, 1060 455 C 900 420, 760 395, 560 360 C 360 318, 200 262, 0 268 Z" fill="var(--swoosh-green)"/>
      <path d="M120 258 C 330 262, 520 310, 700 340 C 840 362, 960 390, 1050 430 C 940 400, 820 382, 690 362 C 500 330, 320 280, 120 258 Z" fill="var(--swoosh-green-light)"/>
      <path d="M560 400 C 760 420, 920 380, 1060 440 C 920 400, 770 440, 560 400 Z" fill="var(--swoosh-green)"/>
    </svg>

    <div class="brand-lockup">
      <span class="brand-square"></span>
      <span class="brand-name">ORB</span>
    </div>

    <ul class="contact-list">
      <li>
        <svg class="contact-icon" viewBox="0 0 16 16"><circle cx="8" cy="8" r="8" fill="#fff"/><path d="M8 3.5 L12.5 7.5 L11.2 7.5 L11.2 12 L4.8 12 L4.8 7.5 L3.5 7.5 Z" fill="var(--band-blue-dark)"/></svg>
        <span>P.O. Box 2047, Fernvale</span>
      </li>
      <li class="address-line-two">VIC 3999</li>
      <li>
        <svg class="contact-icon" viewBox="0 0 16 16"><circle cx="8" cy="8" r="8" fill="#fff"/><path d="M5 4 L7 4 L7.6 6.2 L6.6 7 C7.2 8.4 7.8 9 9 9.6 L9.8 8.6 L12 9.2 L12 11.2 C8 11.6 4.4 8 5 4 Z" fill="var(--band-blue-dark)"/></svg>
        <span>+85 3 8000 4127</span>
      </li>
      <li>
        <svg class="contact-icon" viewBox="0 0 16 16"><circle cx="8" cy="8" r="8" fill="#fff"/><rect x="4" y="6.5" width="8" height="5" fill="var(--band-blue-dark)"/><rect x="5.5" y="4" width="5" height="2.5" fill="var(--band-blue-dark)"/></svg>
        <span>+85 3 8000 4128</span>
      </li>
      <li>
        <svg class="contact-icon" viewBox="0 0 16 16"><circle cx="8" cy="8" r="8" fill="#fff"/><rect x="3.8" y="5" width="8.4" height="6" fill="var(--band-blue-dark)"/><path d="M3.8 5 L8 8.4 L12.2 5" fill="none" stroke="#fff" stroke-width="0.9"/></svg>
        <span>dpalvane@qzr.example</span>
      </li>
      <li>
        <svg class="contact-icon" viewBox="0 0 16 16"><circle cx="8" cy="8" r="8" fill="#fff"/><circle cx="8" cy="8" r="4.6" fill="none" stroke="var(--band-blue-dark)" stroke-width="1"/><path d="M3.4 8 H12.6 M8 3.4 C5.8 6 5.8 10 8 12.6 M8 3.4 C10.2 6 10.2 10 8 12.6" fill="none" stroke="var(--band-blue-dark)" stroke-width="0.9"/></svg>
        <span>www.orbworthkeeping.example</span>
      </li>
    </ul>

    <div class="card-holder">
      <p class="holder-name">Dorotea Wellmont</p>
      <p class="holder-role">Owner / C.E.O.</p>
    </div>
  </div>
</body>
</html>
```